Webdesign für Branchenverzeichnis
Zielgruppe
Wir-bauen-Brücken – das Branchenverzeichnis der Selbstverantwortlichen.
Der Anbieter präsentiert sich mit seinem Namen und der URL - ähnlich wie bei 'blaue Blätter' oder Torkwerk.
Aufgabenstellung
Das Branchenverzeichnis sollte neutral und gleichzeitig hochwertig sein. Die Hauptfarben sind Gold, Schwarz und Weiß. Logo und Corporate Design wurden bereits entwickelt

```html
<!DOCTYPE html>
<html lang="de">
<head>
<meta charset="utf-8">
<title>Wir-bauen-Brücken – Mitgliedschaft</title>
<link href="https://fonts.googleapis.com/css2?family=Quicksand:wght@400;500;600;700&display=swap" rel="stylesheet">
<style>
:root{
  --gold:#d4ad5f;
  --ink:#111;
  --text:#555;
  --muted:#6a6a6a;
  --dark:#3a3a3a;
  --bg:#fbfbfb;
  --line:#d9d9d9;
}
*{box-sizing:border-box;margin:0;padding:0}
html,body{width:1200px;height:850px;overflow:hidden}
body{font-family:'Quicksand',sans-serif;background:var(--bg);position:relative;color:var(--text)}
.site-header{position:absolute;left:0;top:0;width:1200px;height:62px;background:linear-gradient(#2b2b2b,#5a5a5a);box-shadow:0 2px 6px rgba(0,0,0,.25)}
.brand{position:absolute;left:158px;top:21px;display:flex;align-items:center;gap:5px;color:var(--gold);font-weight:700;font-size:9px;white-space:nowrap;width:118px}
.brand-dot{flex:0 0 20px;width:20px;height:20px;border-radius:50%;border:2px solid var(--gold)}
.main-nav a{position:absolute;top:25px;font-size:9px;font-weight:700;letter-spacing:1px;color:#fff;text-decoration:none}
.main-nav a.active{color:var(--gold)}
.icon-box{position:absolute;top:19px;width:25px;height:25px;border:1px solid var(--gold);display:flex;align-items:center;justify-content:center}
.icon-box.user{background:#555}
.cta{position:absolute;left:919px;top:17px;width:125px;height:28px;background:var(--gold);color:#fff;font-size:8px;font-weight:600;letter-spacing:.8px;display:flex;align-items:center;justify-content:center;border-radius:2px}
.hero{position:absolute;left:158px;top:150px;width:440px}
.hero h1{font-size:32px;font-weight:700;letter-spacing:2px;color:var(--ink);white-space:nowrap}
.hero h1 span{color:var(--gold)}
.hero .lead{font-size:16px;letter-spacing:1px;color:#333;margin-top:6px}
.hero p{font-size:11px;line-height:17px;letter-spacing:.8px;margin-top:14px;width:395px;color:var(--muted)}
.hero h2{font-size:11px;font-weight:700;letter-spacing:.8px;color:var(--ink);margin-top:30px}
.hero ol{list-style:none;font-size:11px;line-height:17px;letter-spacing:.6px;width:430px}
.hero ol li{margin-top:17px}
.hero ol li:first-child{margin-top:18px}
.form-card{position:absolute;left:744px;top:113px;width:300px;height:489px;border:2px solid var(--gold);background:#fff;box-shadow:0 2px 10px rgba(0,0,0,.08)}
.tabs{position:absolute;left:18px;top:10px;width:262px;height:14px;font-size:12px;color:#333;letter-spacing:.5px}
.tabs span{position:absolute;top:0}
.tab-track{position:absolute;left:18px;top:29px;width:262px;height:4px;border-radius:2px;background:#eee}
.tab-track i{position:absolute;left:0;top:0;width:70px;height:4px;border-radius:2px;background:var(--gold)}
.field{position:absolute;left:39px;width:219px;height:31px;border:1px solid var(--line);font-size:8px;color:#666;display:flex;align-items:center;justify-content:space-between;padding:0 12px}
.field svg{width:12px;height:12px;fill:none;stroke:var(--gold);stroke-width:1.6;opacity:.55}
.check{position:absolute;left:39px;font-size:8px;color:#666;display:flex;align-items:center;gap:9px}
.check i{width:12px;height:12px;border:1px solid #ccc;border-radius:2px}
.submit{position:absolute;left:39px;top:429px;width:219px;height:31px;background:var(--dark);color:#fff;font-size:8px;font-weight:600;letter-spacing:.8px;display:flex;align-items:center;justify-content:center;border-radius:2px}
.site-footer{position:absolute;left:0;top:660px;width:1200px;height:190px;background:linear-gradient(#5c5c5c,#1f1f1f);color:#fff}
.footer-brand{position:absolute;left:265px;top:48px;width:62px;height:62px;border-radius:50%;border:2px solid #fff}
.footer-col{position:absolute;top:52px}
.footer-col h3{font-size:11px;font-weight:700;letter-spacing:.6px;margin-bottom:14px}
.footer-col p{font-size:9.5px;line-height:16px;width:180px}
.footer-col a{display:block;color:#fff;text-decoration:none;font-size:9.5px;line-height:20.5px}
.footer-col a.under{text-decoration:underline;margin-top:10px}
</style>
</head>
<body>
<header class="site-header">
  <div class="brand"><span class="brand-dot"></span>Wir-bauen-Brücken</div>
  <nav class="main-nav">
    <a style="left:287px">HOME</a>
    <a style="left:362px">SUCHEN</a>
    <a style="left:450px">ÜBER UNS</a>
    <a class="active" style="left:544px">MITGLIEDSCHAFT</a>
    <a style="left:675px">KONTAKT</a>
  </nav>
  <div class="icon-box" style="left:824px">
    <svg width="19" height="12" viewBox="0 0 19 12"><rect width="19" height="4" fill="#000"/><rect y="4" width="19" height="4" fill="#d00"/><rect y="8" width="19" height="4" fill="#fc0"/></svg>
  </div>
  <div class="icon-box user" style="left:857px">
    <svg width="13" height="13" viewBox="0 0 13 13" fill="#fff"><circle cx="6.5" cy="4" r="3"/><path d="M1 13c0-3 2.5-5 5.5-5s5.5 2 5.5 5z"/></svg>
  </div>
  <div class="cta">MITGLIED WERDEN</div>
</header>

<main class="hero">
  <h1>WIR ZEIGEN <span>DEIN UNTERNEHMEN</span></h1>
  <div class="lead">Das Branchenverzeichnis der Selbstverantwortlichen</div>
  <p>Lorem ipsum dolor sit amet, consectetur adipisicing elit, sed do eiusmod tempor incididunt ut labore et dolore magna aliqua. Duis aute irure dolor in reprehenderit in voluptate velit esse cillum dolore eu fugiat nulla pariatur. Ut enim ad minim veniam, quis nostrud</p>
  <h2>WIE WERDE ICH MITGLIED IN 3 EINFACHEN SCHRITTEN?</h2>
  <ol>
    <li>1. Im Formular (rechts von dir) deine Daten eintragen und absenden</li>
    <li>2. Du wirst zu deiner Bank verbunden, um eine Banküberweisung zu tätigen. Für 200€ bekommst du eine Mitgliedschaft für 1 Jahr. Danach wirst du von uns automatisch 4 Wochen vor Ablauf deiner Mitgliedschaft benachrichtigt, ob du die Mitgliedschaft weiter führen möchtest.</li>
    <li>3. Du kannst dich nun mit deiner Email-Adresse und deinem Passwort in unserem Branchenverzeichnis einloggen und deinen eigenen Eintrag erstellen.</li>
  </ol>
</main>

<section class="form-card">
  <div class="tabs"><span style="left:0">Registrieren</span><span style="left:90px">Login</span></div>
  <div class="tab-track"><i></i></div>
  <div class="field" style="top:52px">Vor- und Nachname<svg viewBox="0 0 12 12"><circle cx="6" cy="6" r="5"/><circle cx="6" cy="5" r="1.8"/></svg></div>
  <div class="field" style="top:93px">Firmenname<svg viewBox="0 0 12 12"><rect x="1" y="2" width="10" height="9"/><path d="M4 5h1M7 5h1M4 8h1M7 8h1"/></svg></div>
  <div class="field" style="top:133px">Firmenadresse eingeben<svg viewBox="0 0 12 12"><circle cx="6" cy="6" r="4"/><circle cx="6" cy="6" r="1.3"/><path d="M6 0v2M6 10v2M0 6h2M10 6h2"/></svg></div>
  <div class="field" style="top:174px">Email-Adresse<svg viewBox="0 0 12 12"><circle cx="6" cy="6" r="2"/><path d="M8 6v1a2 2 0 0 0 3-1A5 5 0 1 0 9 10"/></svg></div>
  <div class="field" style="top:214px">Passwort<svg viewBox="0 0 12 12"><path d="M1 6l3.5 3.5L11 3"/></svg></div>
  <div class="field" style="top:255px">Branche wählen<svg viewBox="0 0 12 12"><path d="M1 4l5 5 5-5"/></svg></div>
  <div class="field" style="top:295px">Paket: Mitgliedschaft für 1 Jahr (200€)<svg viewBox="0 0 12 12"><rect x="0.5" y="2" width="11" height="8"/><path d="M0.5 5h11"/></svg></div>
  <div class="field" style="top:336px">Bezahlung: Banküberweisung<svg viewBox="0 0 12 12"><path d="M1 8h7M6 6l2 2-2 2M11 4H4M6 2 4 4l2 2"/></svg></div>
  <label class="check" style="top:378px"><i></i>Ich akzeptiere die DSGVO</label>
  <label class="check" style="top:397px"><i></i>Ich akzeptiere die AGB</label>
  <div class="submit">MITGLIEDSCHAFT KAUFEN</div>
</section>

<footer class="site-footer">
  <div class="footer-brand"></div>
  <div class="footer-col" style="left:359px">
    <h3>WIR BAUEN BRÜCKEN</h3>
    <p>Duis sed odio sit amet nibh vulputate cursus a sit amet mauris Morbi accu.</p>
    <a class="under">Über uns</a>
  </div>
  <div class="footer-col" style="left:647px">
    <h3>WEBSITE</h3>
    <a>Unternehmen suchen</a><a>Mitgliedschaft</a><a>Kontakt</a>
  </div>
  <div class="footer-col" style="left:839px">
    <h3>RECHTLICHES</h3>
    <a>Impressum</a><a>Datenschutz</a><a>AGB</a>
  </div>
</footer>
</body>
</html>
```